Webdesign für Gutshof
Zielgruppe
Gutshof Brandlinger:
Zielgruppe sind alle, die gern Fisch essen. Es gibt einen Hofladen, einen Partyservice, eine Gaststätte und eine kleine Pension. Wichtig wäre darzustellen, dass es in der Gaststätte außer Fisch auch Fleisch gibt.
Einen Einblick geben Ihnen die Webseite und der beiliegende Flyer.
Aufgabenstellung
Die Öffnungszeiten von Gaststätte und Hofladen sollten prominent dargestellt werden. Neben den eigenen Bildern sollen auch stock-Fotos genutzt werden.

```html
<!DOCTYPE html>
<html lang="de">
<head>
<meta charset="utf-8">
<title>Gutshof Brandlinger – Aktuelles &amp; Öffnungszeiten</title>
<link rel="stylesheet" href="https://fonts.googleapis.com/css2?family=Overpass:wght@400;600;700&family=Source+Serif+4:opsz,wght@8..60,400;8..60,500&display=swap">
<style>
  :root {
    --navy: #012c42;
    --ink: #0d3a5c;
    --text: #1f2a33;
    --card: #eeeff0;
    --sky: #0a9be0;
    --sand: #e6dcc3;
    --leaf: #d9cba6;
    --fish: #e3e8eb;
    --white: #ffffff;
  }
  * { box-sizing: border-box; margin: 0; padding: 0; }
  html, body { width: 1200px; height: 850px; overflow: hidden; background: var(--white); }
  body { position: relative; font-family: "Overpass", sans-serif; color: var(--text); }

  .news { position: absolute; left: 0; top: 0; width: 1200px; height: 472px; background: var(--navy); }
  .news__title { position: absolute; top: 56px; width: 100%; text-align: center;
    font-family: "Source Serif 4", serif; font-weight: 400; font-size: 37px; color: var(--white); }
  .news__lead { position: absolute; top: 109px; width: 100%; text-align: center; font-size: 12px; color: var(--white); }

  .leaves { position: absolute; background: radial-gradient(ellipse at center, rgba(217,203,166,.35), rgba(217,203,166,0) 70%); }
  .leaves--left { left: 175px; top: 155px; width: 150px; height: 170px; }
  .leaves--right { left: 895px; top: 162px; width: 140px; height: 170px; }

  .news-card { position: absolute; left: 306px; top: 161px; width: 608px; height: 147px;
    background: var(--card); border-radius: 7px; padding: 22px 26px; }
  .news-card__date { font-size: 10px; font-weight: 600; color: var(--sky); }
  .news-card__title { margin-top: 8px; font-family: "Source Serif 4", serif; font-weight: 400; font-size: 19px; color: var(--ink); }
  .news-card__text { margin-top: 10px; font-size: 12px; line-height: 20px; color: var(--text); }

  .btn { position: absolute; left: 514px; top: 345px; width: 205px; height: 38px; border-radius: 19px;
    background: var(--sky); color: var(--white); font-family: "Source Serif 4", serif; font-size: 16px;
    display: flex; align-items: center; justify-content: center; text-decoration: none; }

  .divider { position: absolute; left: 0; top: 472px; width: 1200px; height: 7px; background: var(--sand); }

  .hours { position: absolute; left: 0; top: 479px; width: 1200px; height: 371px; background: var(--white); }
  .fish-art { position: absolute; left: 940px; top: 208px; width: 260px; height: 163px;
    background: linear-gradient(100deg, var(--fish), rgba(227,232,235,.4)); border-radius: 60% 30% 0 0; }
  .hours__intro { position: absolute; left: 195px; top: 138px; width: 300px; text-align: center; }
  .hours__title { font-family: "Source Serif 4", serif; font-weight: 400; font-size: 42px; line-height: 42px; color: var(--ink); }
  .hours__desc { margin-top: 24px; font-size: 11.5px; line-height: 19px; color: var(--text); }

  .schedule { position: absolute; left: 616px; width: 293px; }
  .schedule--inn { top: 80px; }
  .schedule--shop { top: 280px; }
  .schedule__name { font-family: "Source Serif 4", serif; font-weight: 400; font-size: 21px; color: var(--ink);
    padding-bottom: 8px; border-bottom: 1px solid var(--sand); }
  .schedule__table { margin-top: 14px; border-collapse: collapse; font-size: 13px; }
  .schedule__table td { height: 30px; padding-left: 2px; }
  .schedule__day { width: 155px; font-weight: 700; color: var(--ink); }
  .schedule__time { color: var(--ink); }
</style>
</head>
<body>
  <section class="news">
    <h2 class="news__title">Aktuelles</h2>
    <p class="news__lead">Lorem ipsum dolor sit amet, consetetur sadipscing elitr</p>
    <div class="leaves leaves--left" role="img" aria-label="Gezeichneter Zweig als Dekoration"></div>
    <div class="leaves leaves--right" role="img" aria-label="Gezeichneter Zweig als Dekoration"></div>
    <article class="news-card">
      <p class="news-card__date">26.09.2021</p>
      <h3 class="news-card__title">Information 1</h3>
      <p class="news-card__text">Lorem ipsum dolor sit amet, consetetur sadipscing elitr, sed diam nonumy eirmod tempor invidunt ut labore et dolore magna aliquyam erat, sed diam voluptua.</p>
    </article>
    <a class="btn" href="#">Alle News ansehen »</a>
  </section>

  <div class="divider"></div>

  <section class="hours">
    <div class="fish-art" role="img" aria-label="Zarte Fischzeichnung als Dekoration"></div>
    <div class="hours__intro">
      <h2 class="hours__title">Unsere Öffnungszeiten</h2>
      <p class="hours__desc">Hier finden Sie unsere aktuellen Öffnungszeiten der Hofgaststätte &amp; des Hofladens.</p>
    </div>
    <div class="schedule schedule--inn">
      <h3 class="schedule__name">Hofgaststätte</h3>
      <table class="schedule__table">
        <tr><td class="schedule__day">Freitag</td><td class="schedule__time">Ab 17.00 Uhr</td></tr>
        <tr><td class="schedule__day">Samstag</td><td class="schedule__time">Ab 11.00 Uhr</td></tr>
        <tr><td class="schedule__day">Sonntag</td><td class="schedule__time">11.00 - 14.00 Uhr</td></tr>
        <tr><td class="schedule__day">An Feiertagen</td><td class="schedule__time">11.00 - 14.00 Uhr</td></tr>
      </table>
    </div>
    <div class="schedule schedule--shop">
      <h3 class="schedule__name">Hofladen</h3>
    </div>
  </section>
</body>
</html>
```